Business card update

Opening a subsidiary of my company in the USA and need to update my logo.

Reason: Give more time to a good design.

I made a mistake on my briefing. It's only the business card. Thanks for alerting me on the mistake.

All the best

Teodoro

Target Market(s)

We are an Executive Search company and our target audience are executives in large corporations.

Industry/Entity Type

Business

Requirements
Must have
• Keep the logo. In the US the company is called Dalwick Torren Executive Search.

```html
<!DOCTYPE html>
<html lang="en">
<head>
<meta charset="utf-8">
<title>Dalwick Torren Executive Search – Business Card</title>
<link rel="stylesheet" href="https://fonts.googleapis.com/css2?family=Libre+Baskerville:wght@400;700&display=swap">
<style>
  :root {
    --backdrop: #3a3a3c;
    --teal-dark: #25444c;
    --gold: #efbb1a;
    --paper: #ffffff;
    --ink: #233f46;
    --brand: #2aa5a8;
    --rule: #9ccf7a;
  }
  html, body {
    margin: 0;
    padding: 0;
    width: 1200px;
    height: 1029px;
    overflow: hidden;
    background: var(--backdrop);
  }
  .canvas {
    position: relative;
    width: 1200px;
    height: 1029px;
  }
  .business-card {
    position: absolute;
    left: 100px;
    top: 229px;
    width: 1000px;
    height: 571px;
    border-radius: 6px;
    overflow: hidden;
    font-family: "Libre Baskerville", Georgia, serif;
    color: var(--ink);
  }
  .card-shapes {
    position: absolute;
    inset: 0;
  }
  .contact-block {
    position: absolute;
    left: 70px;
    top: 78px;
    width: 540px;
  }
  .person-name {
    margin: 0;
    font-size: 34px;
    font-weight: 700;
    letter-spacing: 3px;
  }
  .company-name {
    margin: 40px 0 8px;
    font-size: 18px;
    font-weight: 700;
    letter-spacing: 1.5px;
  }
  .address {
    margin: 0;
    font-size: 17px;
    line-height: 30px;
    letter-spacing: 1.5px;
  }
  .divider {
    width: 340px;
    height: 2px;
    margin: 28px 0 34px;
    background: var(--rule);
  }
  .contact-list {
    margin: 0;
    display: grid;
    grid-template-columns: 150px 1fr;
    row-gap: 24px;
    font-size: 17px;
    letter-spacing: 1px;
  }
  .contact-list dt { font-weight: 700; font-size: 19px; }
  .contact-list dd { margin: 0; }
  .brand-band {
    position: absolute;
    left: 640px;
    top: 222px;
    width: 360px;
    height: 70px;
    background: var(--paper);
    display: flex;
    align-items: center;
    justify-content: center;
    gap: 12px;
  }
  .brand-dot {
    width: 16px;
    height: 16px;
    border-radius: 50%;
    background: var(--brand);
  }
  .brand-name {
    font-size: 22px;
    font-weight: 400;
    letter-spacing: 4px;
    color: var(--brand);
    text-transform: uppercase;
  }
</style>
</head>
<body>
<main class="canvas">
  <article class="business-card">
    <svg class="card-shapes" width="1000" height="571" viewBox="0 0 1000 571" aria-hidden="true">
      <rect class="shape-base" width="1000" height="571" fill="var(--teal-dark)"/>
      <path class="shape-gold" d="M0 0 H590 Q680 0 680 90 V481 Q680 571 590 571 H0 Z" fill="var(--gold)"/>
      <path class="shape-panel" d="M0 22 H590 Q645 22 645 77 V465 Q645 520 590 520 H0 Z" fill="var(--paper)"/>
    </svg>

    <section class="contact-block">
      <h1 class="person-name">Teodoro S. Varela</h1>
      <p class="company-name">Dalwick Torren Executive Search</p>
      <p class="address">4820 Harbor View Ave, Suite 300<br>Coral Point, FL 33900</p>
      <div class="divider"></div>
      <dl class="contact-list">
        <dt>Tel:</dt><dd>(555) 014-2870</dd>
        <dt>Web:</dt><dd>www.dtexecutivesearch.com</dd>
        <dt>Email:</dt><dd>tvarela@dtexecutivesearch.com</dd>
      </dl>
    </section>

    <div class="brand-band">
      <span class="brand-dot"></span>
      <span class="brand-name">Dalwick Torren</span>
    </div>
  </article>
</main>
</body>
</html>
```